Small business updating business cards

We have already updated our logo via Pixel Forum and downloaded it (hopefully) for you to use. Now an updated set of business cards for Neil Pollard and Stuart Pollard are also needed... we are also hoping that a copy of our outdated business card designs have uploaded successfully as Microsoft Publisher files. Our Strength Through Unity motto has died a slow death so we are hoping to remove it (and other superfluous lingo if the graphic covers the idea) and instead opt for a fancy graphic (?) on the second side of the card that really reflects our desire to obtain product / haulage from Road Transport / Yard Operators and convert legs of their haulage to rail freight where profitable (bulk haulage / containterised etc). Can you help us look larger, bolder and more robust than we really are (two man show)?
Target Market(s)
Transport Industry
Industry/Entity Type
Business
Contact Information for Business Card
Card details for both N Pollard and S Pollard have been uploaded on the publisher files
Colors
Designer to choose colors to be used in the design.
Requirements
Must have
- Similar theme both sides of card
Should not have
- Black on one side white on the other

```html
<!DOCTYPE html>
<html lang="en">
<head>
<meta charset="utf-8">
<title>Lynford Freight business cards</title>
<link href="https://fonts.googleapis.com/css2?family=Roboto:wght@400;500&family=Exo+2:wght@700&display=swap" rel="stylesheet">
<style>
  :root {
    --backdrop: #e6e3df;
    --card: #1f1f21;
    --emboss: #3a3a3d;
    --gold: #e0b21c;
    --blue: #2aa6cc;
    --steel: #2b3a44;
    --white: #f2f2f2;
  }
  * { box-sizing: border-box; margin: 0; padding: 0; }
  html, body { width: 1200px; height: 715px; overflow: hidden; }
  body {
    background: var(--backdrop);
    font-family: "Roboto", Arial, sans-serif;
    position: relative;
  }
  .card {
    position: absolute;
    top: 203px;
    width: 540px;
    height: 309px;
    background: var(--card);
    border-radius: 4px;
    box-shadow: 0 10px 24px rgba(0,0,0,.28);
    overflow: hidden;
  }
  .card--back { left: 40px; }
  .card--front { left: 620px; }

  /* Back */
  .back-name {
    position: absolute;
    top: 40px; left: 0; right: 0;
    text-align: center;
    font-family: "Exo 2", Arial, sans-serif;
    font-weight: 700;
    font-size: 50px;
    color: var(--emboss);
    letter-spacing: -0.5px;
  }
  .back-contacts {
    position: absolute;
    top: 124px; left: 0; right: 0;
    text-align: center;
    color: var(--gold);
    font-size: 14px;
    line-height: 1.55;
  }
  .road-rail-graphic {
    position: absolute;
    left: 0; right: 0; bottom: 0;
    height: 112px;
    background: linear-gradient(100deg, var(--steel) 0%, #24526a 45%, var(--blue) 75%, var(--gold) 100%);
    opacity: .85;
  }

  /* Front */
  .brand-name {
    position: absolute;
    top: 34px; left: 30px;
    font-family: "Exo 2", Arial, sans-serif;
    font-weight: 700;
    font-size: 38px;
    color: var(--blue);
    line-height: 1;
  }
  .person {
    position: absolute;
    top: 112px; left: 30px;
  }
  .person-name {
    font-size: 20px;
    font-weight: 500;
    color: var(--blue);
  }
  .person-title {
    font-size: 9px;
    color: var(--white);
    margin-top: 1px;
  }
  .rule {
    position: absolute;
    top: 152px; left: 150px;
    width: 360px; height: 1.5px;
    background: linear-gradient(90deg, var(--gold), var(--blue));
  }
  .contact-list {
    position: absolute;
    top: 170px; left: 30px;
    list-style: none;
    color: var(--white);
    font-size: 13px;
    line-height: 1.6;
  }
  .contact-list li { display: flex; align-items: center; gap: 8px; }
  .contact-list .no-icon { padding-left: 20px; }
  .contact-list svg { width: 12px; height: 12px; flex: none; }
  .services {
    position: absolute;
    right: 30px; bottom: 28px;
    text-align: right;
    color: var(--white);
    font-size: 14px;
    line-height: 1.45;
  }
  .services .web-domain { color: var(--gold); }
  .edge-tab {
    position: absolute;
    right: -18px; top: 120px;
    width: 36px; height: 36px;
    border-radius: 50%;
    background: var(--blue);
  }
</style>
</head>
<body>

  <section class="card card--back" aria-label="Card back">
    <div class="back-name">Lynford Freight</div>
    <div class="back-contacts">
      <p>www.lynfordfreight.com.au</p>
      <p>lynford@postbay.com &nbsp;|&nbsp; lynford@mailnest.com</p>
    </div>
    <div class="road-rail-graphic" role="img" aria-label="Graphic of road haulage trucks handing containers and bulk freight over to a freight train on rail"></div>
  </section>

  <section class="card card--front" aria-label="Card front">
    <div class="brand-name">Lynford Freight</div>

    <div class="person">
      <div class="person-name">Neil Pollard</div>
      <div class="person-title">Managing Director</div>
    </div>

    <div class="rule"></div>

    <ul class="contact-list">
      <li class="no-icon">14 Ferndale Street</li>
      <li class="no-icon">Marsden Bay NSW 2290</li>
      <li>
        <svg viewBox="0 0 12 12" aria-hidden="true"><path d="M2 1h2.5l1 2.5-1.5 1a6 6 0 0 0 3.5 3.5l1-1.5 2.5 1V10a1 1 0 0 1-1 1A9 9 0 0 1 1 2a1 1 0 0 1 1-1z" fill="var(--blue)"/></svg>
        0400 555 018
      </li>
      <li>
        <svg viewBox="0 0 12 12" aria-hidden="true"><rect x="0.5" y="2" width="11" height="8" rx="1" fill="var(--blue)"/><path d="M1 2.5l5 4 5-4" stroke="var(--card)" stroke-width="1" fill="none"/></svg>
        pollardn@lynfordfreight.com.au
      </li>
    </ul>

    <div class="services">
      <p>Strategic Alliance Partners &laquo;</p>
      <p>Providing Logistical &laquo;</p>
      <p>Freight Solutions</p>
      <p>www.<span class="web-domain">lynfordfreight</span>.com.au</p>
    </div>

    <div class="edge-tab"></div>
  </section>

</body>
</html>
```